Sticker Design for Supplement Bottle

We want to create a circular sticker design (1 in x 1 in) that simply says: RT's Finds
We want it to be clear or white with gold in it OR clear or white with silver (metallic) colors
We provide reference samples that we like (see attached).
These stickers will go on the top of a supplement bottle
We also attached 3 font styles that we like so providing the sticker using those font styles are most ideal! But stick with white/clear stickers with metallic gold or silver text
Target Market(s)
men and women looking to get healthy
Look and feel
Each slider illustrates characteristics of the customer's brand and the style your logo design should communicate.

```html
<!DOCTYPE html>
<html lang="en">
<head>
<meta charset="utf-8">
<title>RT's Finds – Bottle Cap Sticker</title>
<link rel="stylesheet" href="https://fonts.googleapis.com/css2?family=Domine:wght@700&family=Montserrat:wght@500&display=swap">
<style>
  :root {
    --backdrop: #e4e2e0;
    --sticker-fill: #f1f0ee;
    --sticker-edge: #cfcdcb;
    --gold-light: #f6dc45;
    --gold-mid: #e8c524;
    --gold-deep: #d2aa16;
  }
  html, body {
    margin: 0;
    padding: 0;
    width: 1200px;
    height: 1200px;
    overflow: hidden;
    background: var(--backdrop);
  }
  .sticker {
    display: block;
    width: 1200px;
    height: 1200px;
  }
  .sticker-disc {
    fill: var(--sticker-fill);
    stroke: var(--sticker-edge);
    stroke-width: 2;
  }
  .gold-stop-light { stop-color: var(--gold-light); }
  .gold-stop-mid { stop-color: var(--gold-mid); }
  .gold-stop-deep { stop-color: var(--gold-deep); }
  .crown-arc {
    fill: none;
    stroke: url(#gold-foil);
    stroke-width: 9;
    stroke-linecap: butt;
  }
  .brand-initials,
  .brand-word {
    font-family: "Domine", Georgia, serif;
    font-weight: 700;
    fill: url(#gold-foil);
    text-anchor: middle;
  }
  .brand-initials { font-size: 290px; }
  .brand-word { font-size: 270px; }
  .web-address {
    font-family: "Montserrat", "Century Gothic", sans-serif;
    font-weight: 500;
    font-size: 52px;
    fill: var(--gold-mid);
    letter-spacing: 1px;
  }
</style>
</head>
<body>
  <svg class="sticker" viewBox="0 0 1200 1200" xmlns="http://www.w3.org/2000/svg" role="img" aria-label="RT's Finds round gold sticker">
    <defs>
      <linearGradient id="gold-foil" x1="0" y1="0" x2="1" y2="1">
        <stop class="gold-stop-light" offset="0"/>
        <stop class="gold-stop-mid" offset="0.55"/>
        <stop class="gold-stop-deep" offset="1"/>
      </linearGradient>
      <path id="address-track" d="M 250,600 A 350 350 0 0 0 950,600"/>
    </defs>

    <circle class="sticker-disc" cx="600" cy="600" r="440"/>

    <path class="crown-arc" d="M 248,500 A 366 366 0 0 1 952,500"/>

    <text class="brand-initials" x="600" y="532">RT</text>
    <text class="brand-word" x="600" y="735" textLength="680" lengthAdjust="spacingAndGlyphs">FINDS</text>

    <text class="web-address">
      <textPath href="#address-track" startOffset="50%" text-anchor="middle">www.RTFindsOnline.com</textPath>
    </text>
  </svg>
</body>
</html>
```